Business Card design for new private practice opening

I need a business card design for my new private practice with my new logo uploaded as a file
On the front the logo
On the back: maybe a small logo somewhere?
Priv. Doz. DDr. Corinna Vestaluk
Fachärztin für Allgemein- & Viszeralchirurgie
Address: xxx
Tel: xxx
Mobil:xxx
Webseite:xxx
Email:xxx

Contact Information for Business Card

See project description above for details

Requirements
Nice to have
• I would like the colors of the logo incorporated into the business card

```html
<!DOCTYPE html>
<html lang="de">
<head>
<meta charset="UTF-8">
<title>Vestaluk Chirurgie – Visitenkarte</title>
<link rel="stylesheet" href="https://fonts.googleapis.com/css2?family=Montserrat:wght@400;600&display=swap">
<style>
  :root {
    --backdrop: #e6e6e6;
    --card: #ffffff;
    --teal: #4fbcb3;
    --grey-brand: #7d7d7d;
    --grey-text: #5a5a5a;
  }
  * { margin: 0; padding: 0; box-sizing: border-box; }
  html, body {
    width: 1200px;
    height: 1200px;
    overflow: hidden;
    background: var(--backdrop);
    font-family: "Montserrat", Arial, sans-serif;
  }
  .canvas {
    width: 1200px;
    height: 1200px;
    display: flex;
    align-items: center;
    justify-content: center;
    gap: 90px;
  }
  .card {
    position: relative;
    width: 430px;
    height: 680px;
    background: var(--card);
    box-shadow: 0 8px 24px rgba(0,0,0,0.08);
    display: flex;
    flex-direction: column;
    align-items: center;
  }
  /* Front */
  .card-front { justify-content: flex-start; padding-top: 200px; }
  .brand-mark {
    width: 120px;
    height: 120px;
    border-radius: 50%;
    background: var(--teal);
  }
  .brand-name {
    margin-top: 36px;
    font-weight: 600;
    font-size: 44px;
    line-height: 1.08;
    letter-spacing: 1px;
    text-align: center;
    text-transform: uppercase;
    color: var(--grey-brand);
  }
  .accent-band {
    position: absolute;
    left: 0; right: 0; bottom: 0;
    height: 24px;
    background: var(--teal);
  }
  /* Back */
  .card-back { padding-top: 60px; }
  .brand-small {
    display: flex;
    flex-direction: column;
    align-items: center;
    gap: 10px;
  }
  .brand-small .brand-mark { width: 78px; height: 78px; }
  .brand-small-name {
    font-weight: 600;
    font-size: 13px;
    letter-spacing: 1px;
    text-transform: uppercase;
    color: var(--grey-brand);
  }
  .person {
    margin-top: 40px;
    text-align: center;
    color: var(--grey-text);
  }
  .person-title, .person-name {
    font-weight: 400;
    font-size: 29px;
    line-height: 1.15;
  }
  .person-specialty {
    margin-top: 8px;
    font-size: 18px;
    line-height: 1.25;
  }
  .contact {
    margin-top: 62px;
    list-style: none;
    text-align: center;
    font-size: 19px;
    line-height: 1.3;
    color: var(--grey-text);
  }
</style>
</head>
<body>
<main class="canvas">
  <section class="card card-front" aria-label="Vorderseite">
    <div class="brand-mark" aria-hidden="true"></div>
    <h1 class="brand-name">Vestaluk<br>Chirurgie</h1>
    <div class="accent-band"></div>
  </section>

  <section class="card card-back" aria-label="Rückseite">
    <div class="brand-small">
      <div class="brand-mark" aria-hidden="true"></div>
      <span class="brand-small-name">Vestaluk Chirurgie</span>
    </div>
    <div class="person">
      <p class="person-title">Priv. Doz. DDr.</p>
      <p class="person-name">Corinna Vestaluk</p>
      <p class="person-specialty">Fachärztin für Allgemein-<br>&amp; Viszeralchirurgie</p>
    </div>
    <ul class="contact">
      <li>Address: xxx</li>
      <li>Tel: xxx</li>
      <li>Mobil: xxx</li>
      <li>Webseite: xxx</li>
      <li>Email: xxx</li>
    </ul>
  </section>
</main>
</body>
</html>
```